Creative Businesss Card desgin!

Create a business card for our business Gleam window cleaning!
We are open to creative ideas as long as it maintains a professional image.

Target Market(s)

Small Commercial window cleaning clients including car dealerships, strata manager, cafe

Industry/Entity Type

Window Cleaning

Contact Information for Business Card

Daniel Prescott
General Manager
Gleam Window Cleaning

daniel@gleamservices.com.au
pane-care-southbank.com.au
Ph: 1800 GET GLEAM
Mob: 0437 582 061

Colors
fbed22
0392cd

Requirements
Should not have
• Stock window cleaning/ squeegee graphics

```html
<!DOCTYPE html>
<html lang="en">
<head>
<meta charset="utf-8">
<title>Gleam Window Cleaning – Business Card</title>
<link href="https://fonts.googleapis.com/css2?family=Hind:wght@400;600;700&display=swap" rel="stylesheet">
<style>
  :root {
    --brand-blue: #0a4fad;
    --brand-yellow: #eef21f;
    --ink: #1a1a1a;
    --band: #18181a;
    --paper: #ffffff;
  }
  html, body {
    margin: 0;
    padding: 0;
    overflow: hidden;
    background: var(--paper);
  }
  .canvas {
    position: relative;
    width: 1029px;
    height: 1200px;
    overflow: hidden;
    background: var(--paper);
    font-family: "Hind", Arial, sans-serif;
  }
  .shapes {
    position: absolute;
    inset: 0;
  }
  .card-front__details {
    position: absolute;
    right: 45px;
    top: 72px;
    text-align: right;
    color: var(--ink);
  }
  .person-name {
    margin: 0;
    font-size: 52px;
    font-weight: 700;
    line-height: 1;
    color: var(--brand-blue);
  }
  .person-title {
    margin: 2px 0 0;
    font-size: 32px;
    font-weight: 700;
    line-height: 1.1;
    color: var(--brand-blue);
  }
  .company-name {
    margin: 118px 0 0;
    font-size: 34px;
    font-weight: 700;
    line-height: 1.1;
    color: var(--brand-blue);
  }
  .contact-line {
    margin: 4px 0 0;
    font-size: 30px;
    font-weight: 400;
    line-height: 1.45;
  }
  .contact-label {
    color: var(--brand-blue);
  }
  .website {
    position: absolute;
    left: 128px;
    top: 490px;
    margin: 0;
    font-size: 37px;
    font-weight: 400;
    color: var(--brand-yellow);
  }
  .brand-name {
    position: absolute;
    margin: 0;
    font-weight: 700;
    text-align: center;
    line-height: 0.95;
  }
  .brand-name--front {
    left: 60px;
    top: 190px;
    width: 460px;
    color: var(--brand-yellow);
    transform: rotate(-32deg);
  }
  .brand-name--back {
    left: 279px;
    top: 850px;
    width: 471px;
    color: var(--paper);
  }
  .brand-name__main {
    display: block;
    font-size: 110px;
    letter-spacing: 2px;
  }
  .brand-name__sub {
    display: block;
    font-size: 40px;
    letter-spacing: 1px;
  }
</style>
</head>
<body>
<div class="canvas">
  <svg class="shapes" width="1029" height="1200" viewBox="0 0 1029 1200" aria-hidden="true">
    <!-- front: contact band -->
    <rect class="front-band" x="0" y="477" width="1029" height="111" fill="var(--band)"/>
    <!-- front: white separation under the brand panel -->
    <polygon points="0,0 376,0 527,208 0,542" fill="var(--paper)"/>
    <!-- front: brand panel edge line -->
    <polyline points="382,0 534,211 118,477" fill="none" stroke="var(--band)" stroke-width="6"/>
    <!-- front: brand panel -->
    <polygon class="front-panel" points="0,0 370,0 519,206 0,534" fill="var(--brand-blue)"/>
    <!-- back: hourglass panel -->
    <polygon class="back-panel"
             points="0,612 1029,612 750,845 750,1001 1029,1200 0,1200 279,1001 279,845"
             fill="var(--brand-blue)"/>
  </svg>

  <section class="card-front">
    <p class="brand-name brand-name--front">
      <span class="brand-name__main">GLEAM</span>
      <span class="brand-name__sub">WINDOW CLEANING</span>
    </p>
    <div class="card-front__details">
      <h1 class="person-name">Daniel Prescott</h1>
      <p class="person-title">General Manager</p>
      <p class="company-name">Gleam Window Cleaning</p>
      <p class="contact-line">#1800 GET GLEAM<br>
        <span class="contact-label">Mobile :</span> 0437 582 061<br>
        <span class="contact-label">E-mail :</span> daniel@gleamservices.com.au</p>
    </div>
    <p class="website">www.pane-care-southbank.com.au</p>
  </section>

  <section class="card-back">
    <p class="brand-name brand-name--back">
      <span class="brand-name__main">GLEAM</span>
      <span class="brand-name__sub">WINDOW CLEANING</span>
    </p>
  </section>
</div>
</body>
</html>
```